Need Bold, Hip Card for Concert Ticket Website Velvet Stubs!

Hi there! I am putting together a business/website that sells event tickets (mostly concerts, but also some sports and theater). Think PassDepot, but much smaller. The site is called Velvet Stubs. I have a new logo (attached, with black/red/white color scheme), and am looking for a modern/cool/original business card design. Note that I am thinking of having the card itself in the shape of a ticket (die cut), so you may want to keep that in mind when designing, but I'm not set on that. I'm also open to alternative card sizes, thicknesses, glossy, spot UV, etc. in order to stand out. I'm attaching a potential die cut template and a sample card using that template in case you want to work with that.
Target Market(s)
Music fans, people that like going to see live events
Industry/Entity Type
Entertainment
Contact Information for Business Card
Information that I'd like to have:
website address - www.velvetstubs-example.com
phone number: 1-833-5VELVETS (835-3887)
my name - Delia Hart
Look and feel
Each slider illustrates characteristics of the customer's brand and the style your logo design should communicate.

```html
<!DOCTYPE html>
<html lang="en">
<head>
<meta charset="utf-8">
<title>Velvet Stubs – Business Card</title>
<link rel="stylesheet" href="https://fonts.googleapis.com/css2?family=Montserrat:wght@600;700&family=Roboto:wght@500&display=swap">
<style>
  :root {
    --stage: #696969;
    --card-dark: #0b0c0e;
    --card-light: #f7f7f7;
    --brand-red: #8b1014;
    --ink: #161616;
    --logo-grey: #8a8a8a;
  }
  * { margin: 0; padding: 0; box-sizing: border-box; }
  html, body { width: 1200px; height: 590px; overflow: hidden; background: var(--stage); }
  .canvas { position: relative; width: 1200px; height: 590px; background: var(--stage); }

  .card { position: absolute; top: 154px; width: 491px; height: 281px; }
  .card--back { left: 94px; }
  .card--front { left: 614px; }
  .card__shape { position: absolute; inset: 0; width: 491px; height: 281px; }
  .card--back .card__shape path { fill: var(--card-dark); }
  .card--front .card__shape path { fill: var(--card-light); }

  .brand-lockup {
    position: absolute; left: 0; right: 0; top: 0; bottom: 0;
    display: flex; align-items: center; justify-content: center; gap: 16px;
  }
  .brand-lockup__mark { width: 52px; height: 52px; background: var(--logo-grey); }
  .brand-lockup__name {
    font-family: "Montserrat", sans-serif; font-weight: 700;
    font-size: 34px; line-height: 1; letter-spacing: 1px;
    color: var(--logo-grey); text-transform: uppercase;
  }

  .perforation {
    position: absolute; left: 32px; width: 406px; height: 0;
    border-top: 2px dashed var(--brand-red);
  }
  .perforation--top { top: 16px; }
  .perforation--bottom { top: 264px; }

  .front-name {
    position: absolute; left: 53px; top: 50px;
    font-family: "Montserrat", sans-serif; font-weight: 700;
    font-size: 40px; line-height: 40px; letter-spacing: 1px;
    color: var(--brand-red); text-transform: uppercase;
  }
  .front-mark {
    position: absolute; left: 318px; top: 74px;
    width: 110px; height: 110px; background: var(--ink);
  }
  .holder-name {
    position: absolute; left: 53px; top: 158px;
    font-family: "Montserrat", sans-serif; font-weight: 600;
    font-size: 20px; letter-spacing: 1px;
    color: var(--brand-red); text-transform: uppercase;
  }
  .contact {
    position: absolute; left: 53px; top: 195px;
    font-family: "Roboto", sans-serif; font-weight: 500;
    font-size: 14px; line-height: 19px; color: var(--ink);
    list-style: none;
  }
</style>
</head>
<body>
<div class="canvas">

  <section class="card card--back" aria-label="Card back">
    <svg class="card__shape" viewBox="0 0 491 281" aria-hidden="true">
      <path d="M32,0 H459 A32 32 0 0 0 491 32 V249 A32 32 0 0 0 459 281 H32 A32 32 0 0 0 0 249 V32 A32 32 0 0 0 32 0 Z"/>
    </svg>
    <div class="brand-lockup">
      <span class="brand-lockup__mark" aria-hidden="true"></span>
      <span class="brand-lockup__name">Velvet Stubs</span>
    </div>
  </section>

  <section class="card card--front" aria-label="Card front">
    <svg class="card__shape" viewBox="0 0 491 281" aria-hidden="true">
      <path d="M32,0 H459 A32 32 0 0 0 491 32 V249 A32 32 0 0 0 459 281 H32 A32 32 0 0 0 0 249 V32 A32 32 0 0 0 32 0 Z"/>
    </svg>
    <div class="perforation perforation--top"></div>
    <div class="perforation perforation--bottom"></div>

    <div class="front-name">Velvet<br>Stubs</div>
    <span class="front-mark" aria-hidden="true"></span>

    <p class="holder-name">Delia Hart</p>
    <ul class="contact">
      <li>1-833-5VELVETS (835-3887)</li>
      <li>www.velvetstubs-example.com</li>
    </ul>
  </section>

</div>
</body>
</html>
```